Migration and redesign of existing website to WordPress using DIVI 3

I. TASK OBJECTIVE:
- Redesign our existing website www.harlowsteppodiatry.com.au with a fresh new look and migrate to new Wordpress site based on DIVI3 theme. The site will contain the same basic functionality as the existing site (with some small changes).

II. STYLE/ DESIGN ASPECT:
As an example of a site that I like the look of, see https://quillmarsh.com/. I like the use of shadows, and this would go well with the little animations you can do with Divi (e.g. when hovering over pics).

1. What I am looking for is a design which has lots of white space, is modern and friendly looking (but still not too cute or frivolous, as we are a medical practice)
2. DESIGN that is NOT TOO rectangular or blocky.
3. Please take into consideration our Users are Older market, so any icons or navigation features need to be very easy to understand and not too small.
4. Must be easy to navigate
5. We are are happy to go with a new colour scheme, and are working on some ideas for this, but happy to take suggestions.

III. SPECIFICATIONS:
1. 5+ Pages (should flow like the current site)
2. Using Wordpress Divi 3 theme.
3. I'd like every page to have a "book now" button and a contact form in a sidebar so that users can click the button or fill in the contact form without scrolling at all. EXCEPT ON THE HOME PAGE, where there should still be a book now button (maybe on the top right in the header of all pages?), and maybe a contact us button which scrolls down to the contact area at the bottom of the HOME page. I don't think a side bar is necessarily required on the home page, but if you think it makes sense from a design perspective please let me know.
4. AT THE BOTTOM OF THE PAGE, just above the FOOTER, I'd like a row of trust logos for various organisations that we are affiliated with. (A list of this company will be provided later but you could temporarily use placeholders)

Once we have a structure in place, we can migrate most of the content. Please let me know if I'm not being clear or you need further information.

Podiatry Customers and Referrors

Health Care

Coded - Design and coding required

5+ page

Designer to choose colors to be used in the design.

• Simple to navigate.
• Contact/booking details on most if not all pages - please see specification above
• Section for Trusted Affiliates above the footer
• Wordpress using Divi3 Theme
• Not too busy with the design. Plenty of white space or light background.
• Should not be complicated to navigate.
• TOO rectangular or blocky designs

```html
<!DOCTYPE html>
<html lang="en">
<head>
<meta charset="utf-8">
<title>Harlow Step Podiatry</title>
<link href="https://fonts.googleapis.com/css2?family=Roboto:wght@300;400;500;700&display=swap" rel="stylesheet">
<style>
:root{
  --blue:#138fc4;
  --blue-light:#12a3d9;
  --teal-dark:#0b6d8f;
  --heading:#1e98b8;
  --text:#6a6a6a;
  --muted:#9a9a9a;
  --line:#e2e2e2;
  --dark:#2c2c2c;
  --darker:#222;
  --navy:#22394a;
  --white:#fff;
}
*{box-sizing:border-box;margin:0;padding:0}
html,body{width:1200px;height:4018px;overflow:hidden}
body{position:relative;background:var(--white);font-family:"Roboto",Arial,sans-serif;color:var(--text);font-size:12px;line-height:1.55}
.section{position:absolute;left:0;width:1200px}
.wrap{position:absolute;left:171px;width:858px}
h2.title{font-weight:400;color:var(--heading);font-size:30px;line-height:1.2}
.kicker{font-size:11px;color:var(--heading);font-weight:500}
.subtitle{font-size:20px;color:#333;font-weight:400}
.arrows{position:absolute;display:flex;gap:6px}
.arrows span{width:20px;height:20px;border:1px solid #ccc;display:flex;align-items:center;justify-content:center;font-size:12px;color:#666;border-radius:2px}
.ph{display:block}

/* header */
.header{top:0;height:107px;border-bottom:1px solid var(--line)}
.brand{position:absolute;left:171px;top:18px;display:flex;align-items:center;gap:10px}
.brand-mark{width:30px;height:30px;border-radius:50%;background:var(--blue)}
.brand-name{font-size:18px;font-weight:500;color:var(--teal-dark)}
.header-divider{position:absolute;left:383px;top:0;width:1px;height:107px;background:var(--line)}
.topbar{position:absolute;left:400px;right:171px;top:0;height:34px;display:flex;align-items:center;gap:22px;font-size:11px;color:#555;border-bottom:1px solid var(--line)}
.topbar .item{display:flex;align-items:center;gap:6px}
.social{display:flex;gap:8px;margin-left:auto}
.social i{width:10px;height:10px;border-radius:50%;background:#7d7d7d;display:block}
.search{width:20px;display:flex;justify-content:center}
.nav{position:absolute;left:400px;right:171px;top:56px;display:flex;justify-content:space-between;font-size:12px;font-weight:500;color:#333}
.nav a{color:#333;text-decoration:none;padding-bottom:12px}
.nav a.active{color:var(--blue);border-bottom:2px solid var(--blue)}

/* hero */
.hero{top:107px;height:402px;background:linear-gradient(100deg,#b9bcbe 0%,#d8d8d6 35%,#c5b7aa 60%,#efe9e3 85%,#f4f1ee 100%)}
.hero-box{position:absolute;left:171px;top:169px;width:365px;height:153px;background:rgba(255,255,255,.82);padding:22px 18px}
.hero-box h1{font-weight:400;font-size:27px;line-height:1.2;color:var(--blue)}
.btn-solid{display:inline-block;margin-top:16px;background:var(--teal-dark);color:#fff;font-size:10px;font-weight:500;padding:7px 11px;letter-spacing:.3px}

/* promo boxes */
.promos{top:461px;height:209px}
.promos .wrap{display:flex;height:209px}
.promo{flex:1;padding:24px 22px;color:#e8f6fb}
.promo h3{font-size:19px;font-weight:400;color:#fff;margin-bottom:12px}
.promo p{font-size:11px;line-height:1.5}
.promo.a{background:var(--blue)}
.promo.b{background:var(--blue-light)}
.promo.c{background:var(--teal-dark)}
.btn-outline{display:inline-block;margin-top:18px;border:1px solid rgba(255,255,255,.8);color:#fff;font-size:10px;padding:6px 10px}
.hours{width:100%;border-collapse:collapse;font-size:10px;color:#fff}
.hours td{padding:7px 0;border-bottom:1px solid rgba(255,255,255,.35)}
.hours td+td{text-align:right}

/* welcome */
.welcome{top:723px;height:350px}
.welcome .intro{position:absolute;top:70px;width:858px;font-size:14px;color:#7a7a7a;line-height:1.45}
.welcome .range{position:absolute;top:123px;font-size:14px;color:#7a7a7a}
.features{position:absolute;top:170px;width:858px;display:flex;gap:24px}
.feature{flex:1}
.feature .icon{width:40px;height:40px;border-radius:8px;background:#d4eef6}
.feature h4{font-size:16px;font-weight:500;color:#333;margin:14px 0 8px}
.feature p{font-size:10px;line-height:1.5;color:#777}
.rule{position:absolute;top:1093px;left:0;width:1200px;height:1px;background:var(--line)}

/* services */
.services{top:1125px;height:340px}
.services h2{font-size:22px;position:absolute;left:10px;top:8px}
.tabs{position:absolute;top:59px;left:0;width:204px}
.tab{height:36px;display:flex;align-items:center;justify-content:center;border:1px solid var(--line);margin-bottom:1px;font-size:13px;color:#444}
.tab.active{background:#f2f6f8}
.services .copy{position:absolute;left:231px;top:55px;width:627px;font-size:10px;line-height:1.55;color:#777}
.carousel{position:absolute;left:228px;top:193px;width:630px;display:flex;gap:10px}
.slide{flex:1;text-align:center;font-size:11px;color:#444}
.slide .ph{height:100px;margin-bottom:8px}
.car-arrow{position:absolute;top:233px;width:18px;height:22px;background:#fff;border:1px solid #ccc;font-size:11px;display:flex;align-items:center;justify-content:center}

/* testimonials */
.testimonials{top:1500px;height:370px;background:linear-gradient(90deg,#1d2f3b,#2b4656 55%,#203542)}
.testimonials .head{position:absolute;top:48px;width:1200px;text-align:center;color:#fff}
.testimonials .head small{font-size:11px;display:block}
.testimonials .head h2{font-size:21px;font-weight:400}
.cards{position:absolute;left:171px;top:118px;width:858px;display:flex;gap:19px}
.tcard{flex:1;background:#fff;height:172px}
.tcard .top{background:var(--blue);height:48px;display:flex;align-items:center;gap:10px;padding:0 10px;color:#fff}
.avatar{width:36px;height:36px;border-radius:50%;background:#c9d6de;border:2px solid #fff}
.tcard .name{font-size:13px}
.tcard .role{font-size:10px;opacity:.85}
.tcard .body{padding:16px 18px;display:flex;gap:10px;font-size:10px;color:#777;line-height:1.5}
.tcard .q{font-size:26px;color:#bbb;line-height:.9;font-family:Georgia,serif}

/* stats */
.stats{top:1875px;height:135px;background:var(--blue);display:flex;padding:0 171px;align-items:center}
.stat{flex:1;text-align:center;color:#fff}
.stat b{display:block;font-size:30px;font-weight:400;line-height:1.2}
.stat span{font-size:13px}

/* doctors */
.doctors{top:2050px;height:460px}
.doctors .subtitle{position:absolute;top:22px}
.doctors .arrows{right:0;top:22px}
.doc-grid{position:absolute;top:75px;width:858px;display:flex;gap:22px}
.doc{flex:1;border:1px solid var(--line);height:376px}
.doc .ph{height:200px;background:linear-gradient(180deg,#f1f1f1,#dcdcdc)}
.doc .inner{padding:10px 12px}
.doc h4{font-size:15px;font-weight:400;color:var(--heading)}
.doc .role{font-size:10px;color:#555}
.doc p{font-size:9px;line-height:1.5;color:#888;margin:14px 0 10px}
.doc .meta{border-top:1px solid var(--line);padding-top:8px;font-size:9px;color:#555}
.doc .meta div{display:flex;align-items:center;gap:6px;margin-bottom:6px}

/* case histories */
.cases{top:2600px;height:320px}
.cases .kicker{position:absolute;top:6px}
.cases .subtitle{position:absolute;top:28px}
.cases .arrows{left:592px;top:30px}
.case-grid{position:absolute;top:74px;width:632px;display:flex;gap:22px}
.case{flex:1}
.case .ph{height:126px}
.case h4{font-size:15px;font-weight:500;color:var(--heading);margin:20px 0 6px}
.case p{font-size:9px;line-height:1.5;color:#888}
.ebook{position:absolute;left:665px;top:20px;width:193px;height:280px;background:var(--blue);overflow:hidden}
.ebook .top{padding:12px 10px;color:#fff}
.ebook h4{font-size:16px;font-weight:500}
.ebook .top p{font-size:8px;line-height:1.4;opacity:.9}
.ebook .ph{height:130px;margin-top:6px}
.ebook .cta{position:absolute;bottom:0;left:0;right:0;height:44px;background:var(--navy);color:#fff;font-size:14px;font-weight:500;display:flex;align-items:center;justify-content:center}

/* booking + faq */
.booking{top:2995px;height:315px}
.book{position:absolute;top:5px;left:0;width:418px;height:300px;background:var(--blue);padding:38px 26px;color:#fff}
.book h3{font-size:19px;font-weight:400;margin-bottom:24px}
.fields{display:grid;grid-template-columns:1fr 1fr;gap:18px 14px}
.field{height:30px;border:1px solid rgba(255,255,255,.55);background:rgba(255,255,255,.1);font-size:10px;display:flex;align-items:center;justify-content:space-between;padding:0 8px}
.book .btn-outline{margin-top:18px}
.faq{position:absolute;left:440px;top:8px;width:418px}
.faq .subtitle{font-size:18px;margin-bottom:14px}
.acc{border:1px solid var(--line);margin-bottom:10px;font-size:12px;color:#333}
.acc .q{height:36px;display:flex;align-items:center;justify-content:space-between;padding:0 12px}
.acc.open .q{color:var(--blue);border-bottom:1px solid var(--line)}
.acc .a{padding:12px;font-size:11px;color:#777;line-height:1.5}

/* partners */
.partners{top:3375px;height:140px;text-align:center}
.partners h3{font-size:20px;font-weight:400;color:#333;margin-top:10px}
.logos{position:absolute;left:185px;top:88px;width:830px;display:flex;justify-content:space-between;align-items:center}
.logos span{display:block;height:28px;background:#d7d7d7;border-radius:3px}

/* newsletter */
.newsletter{top:3563px;height:94px;background:#0f88b9;color:#fff}
.newsletter h3{position:absolute;left:171px;top:25px;font-size:20px;font-weight:400}
.newsletter p{position:absolute;left:171px;top:55px;font-size:11px}
.nl-form{position:absolute;left:611px;top:32px;width:418px;height:32px;display:flex}
.nl-form .in{flex:1;background:#fff;color:#999;font-size:10px;padding:0 10px;display:flex;align-items:center}
.nl-form .go{width:118px;background:#f7f7f7;color:#333;font-size:11px;font-weight:500;display:flex;align-items:center;justify-content:center;border-left:1px solid #ddd}

/* footer */
.footer{top:3657px;height:361px;background:var(--dark);color:#a9a9a9}
.fcols{position:absolute;left:171px;top:48px;width:858px;display:flex;gap:22px}
.fcol{flex:1;font-size:10px}
.fcol h5{font-size:14px;font-weight:400;color:#fff;margin-bottom:10px}
.fcol h5::after{content:"";display:block;width:24px;height:2px;background:var(--blue);margin-top:6px}
.fcol ul{list-style:none}
.fcol li{padding:6px 0;border-bottom:1px solid #3b3b3b;display:flex;align-items:center;gap:6px}
.fcol .cinfo div{display:flex;align-items:center;gap:6px;padding:6px 0}
.fsocial{display:flex;gap:10px;margin-top:8px}
.fsocial i{width:10px;height:10px;border-radius:50%;background:#7a7a7a;display:block}
.qin{height:28px;border:1px solid #474747;background:#333;margin-bottom:10px;padding:6px 8px}
.qin.tall{height:56px}
.qbtn{display:inline-block;border:1px solid #555;color:#ddd;padding:5px 12px}
.copyright{position:absolute;left:0;bottom:0;width:1200px;height:33px;background:var(--darker);font-size:10px;padding-left:171px;display:flex;align-items:center;color:#888}
.to-top{position:absolute;left:1135px;top:3915px;width:28px;height:28px;background:var(--blue);display:flex;align-items:center;justify-content:center}
</style>
</head>
<body>

<header class="section header">
  <div class="brand"><span class="brand-mark"></span><span class="brand-name">Harlow Step Podiatry</span></div>
  <div class="header-divider"></div>
  <div class="topbar">
    <div class="item"><svg width="9" height="12" viewBox="0 0 9 12"><path d="M4.5 0a4.5 4.5 0 0 0-4.5 4.5C0 8 4.5 12 4.5 12S9 8 9 4.5A4.5 4.5 0 0 0 4.5 0zm0 6.3a1.8 1.8 0 1 1 0-3.6 1.8 1.8 0 0 1 0 3.6z" fill="#138fc4"/></svg>42 Wenlock Road, Kellerton, WA 6099</div>
    <div class="item"><svg width="11" height="11" viewBox="0 0 12 12"><path d="M2.4 0l2 2.6-1.2 1.6c.8 1.7 2.1 3 3.8 3.8l1.6-1.2L11.2 9 10 11c-5 0-9.6-4.6-9.6-9.6z" fill="#138fc4"/></svg>(08) 9470 2815</div>
    <div class="social"><i></i><i></i><i></i><i></i></div>
    <div class="search"><svg width="12" height="12" viewBox="0 0 12 12"><circle cx="5" cy="5" r="3.8" stroke="#138fc4" stroke-width="1.6" fill="none"/><path d="M8 8l3.3 3.3" stroke="#138fc4" stroke-width="1.8"/></svg></div>
  </div>
  <nav class="nav">
    <a class="active">Home</a><a>Common Problems</a><a>Services</a><a>About Us</a><a>Case Histories</a><a>Helpful Information</a><a>Blog</a><a>Contact</a>
  </nav>
</header>

<section class="section hero" role="img" aria-label="Podiatrist treating a patient's foot with a therapy device">
  <div class="hero-box">
    <h1>We Offer Solutions To Common Foot Problems</h1>
    <span class="btn-solid">LEARN MORE</span>
  </div>
</section>

<section class="section promos">
  <div class="wrap">
    <div class="promo a">
      <h3>Top Doctors</h3>
      <p>Our experienced team of podiatrists offer caring treatment for every foot and ankle concern, from children to older adults.</p>
      <span class="btn-outline">READ MORE</span>
    </div>
    <div class="promo b">
      <h3>24 Hours Service</h3>
      <p>Urgent foot care is available when you need it most, with a podiatrist on call to help you day and night.</p>
      <span class="btn-outline">READ MORE</span>
    </div>
    <div class="promo c">
      <h3>Opening Hours</h3>
      <table class="hours">
        <tr><td>Monday - Friday</td><td>8.30am - 5.00pm</td></tr>
        <tr><td>Thursday</td><td>8.30am - 7.00pm</td></tr>
        <tr><td>Second Saturday</td><td>8.30am - 12.30pm</td></tr>
      </table>
    </div>
  </div>
</section>

<section class="section welcome">
  <div class="wrap" style="top:0;height:350px">
    <h2 class="title" style="position:absolute;top:18px">Welcome to Harlow Step Podiatry</h2>
    <p class="intro">Clinic was established in 1981 by Dr. Lena Groves. We currently have six podiatrists and two administrative staff members housed in a modern, state-of-the-art clinic, with ample parking on site</p>
    <p class="range">We treat a wide range of conditions</p>
    <div class="features">
      <div class="feature"><div class="icon" role="img" aria-label="Heel icon"></div><h4>Heel and Arch Pain</h4><p>Heel pain is a common presentation that we see as podiatrists. Heel pain is a broad term and can cover many different conditions.</p></div>
      <div class="feature"><div class="icon" role="img" aria-label="Sports shoe icon"></div><h4>Sports Injuries</h4><p>We have been able to relieve many chronic conditions and severe injuries caused by ballet, dancing, professional sports and extreme competitions.</p></div>
      <div class="feature"><div class="icon" role="img" aria-label="Skin and nail icon"></div><h4>Skin and Nail Care</h4><p>We are happy to manage your toenail and skin care, using sterilised instruments. Our podiatrists can trim and file toenails and reduce thickness.</p></div>
      <div class="feature"><div class="icon" role="img" aria-label="Foot surgery icon"></div><h4>Foot and Ankle Surgery</h4><p>All the podiatrists at Harlow Step Podiatry are qualified and competent to perform minor surgical procedures of the foot.</p></div>
    </div>
  </div>
</section>
<div class="rule"></div>

<section class="section services">
  <div class="wrap" style="height:340px">
    <h2 class="title">Our Services</h2>
    <div class="tabs">
      <div class="tab active">Common Problems</div>
      <div class="tab">Foot &amp; Ankle Surgery</div>
      <div class="tab">Sport &amp; Dance</div>
      <div class="tab">All Our Services</div>
    </div>
    <p class="copy">When you suffer from a foot and/or ankle problem, the pain and discomfort can make it a challenge to engage in simple, daily activities. When the pain disrupts your life, you need to contact a skilled, experienced podiatrist to get resolution. The podiatrists at Harlow Step Podiatry offer a variety of treatment options for many common foot and ankle conditions, including Achilles tendon injuries, ankle sprains, flat foot and clawed feet, and bunions and ingrown toenails. Your primary concern is the health of your feet and ankles, and we use advanced equipment and work with other professionals to ensure the best outcome. To discuss your foot and ankle pain, contact our Kellerton office at (08) 9470 2815.</p>
    <div class="carousel">
      <div class="slide"><div class="ph" role="img" aria-label="Achilles tendon injury photo" style="background:linear-gradient(160deg,#cfe3ee,#e8c9b8)"></div>Achilles Tendon Injuries</div>
      <div class="slide"><div class="ph" role="img" aria-label="Bunions photo" style="background:linear-gradient(160deg,#e9d0c2,#c9a490)"></div>Bunions</div>
      <div class="slide"><div class="ph" role="img" aria-label="Corns and calluses photo" style="background:linear-gradient(160deg,#d9b7a3,#b88c74)"></div>Corns and calluses</div>
      <div class="slide"><div class="ph" role="img" aria-label="Ankle sprain photo" style="background:linear-gradient(160deg,#d1d4d6,#a9aeb2)"></div>Ankle Sprains</div>
      <div class="slide"><div class="ph" role="img" aria-label="Fungal nails photo" style="background:linear-gradient(160deg,#ecd9c8,#d2b397)"></div>Fungal Nails</div>
    </div>
    <div class="car-arrow" style="left:219px">‹</div>
    <div class="car-arrow" style="left:849px">›</div>
  </div>
</section>

<section class="section testimonials" role="img" aria-label="Dark blue background of a clinic consultation">
  <div class="head"><small>Testimonials</small><h2>What Our Clients Say</h2></div>
  <div class="cards">
    <div class="tcard"><div class="top"><div class="avatar"></div><div><div class="name">Vera Aldridge</div><div class="role">Podiatric Surgery</div></div></div>
      <div class="body"><span class="q">“</span><p>The team explained everything clearly and my heel pain is finally gone. I can walk every morning again without any discomfort at all.</p></div></div>
    <div class="tcard"><div class="top"><div class="avatar"></div><div><div class="name">Pia D. Sorrel</div><div class="role">Podiatric Surgery</div></div></div>
      <div class="body"><span class="q">“</span><p>Friendly staff and a very calm clinic. My bunion surgery went smoothly and the follow up care was thorough and kind.</p></div></div>
    <div class="tcard"><div class="top"><div class="avatar"></div><div><div class="name">Bennett Ewing</div><div class="role">Podiatric Surgery</div></div></div>
      <div class="body"><span class="q">“</span><p>After my ankle sprain they built a simple plan that got me back on the field quickly. Highly recommend this practice.</p></div></div>
  </div>
</section>

<section class="section stats">
  <div class="stat"><b>36</b><span>Years of Experience</span></div>
  <div class="stat"><b>6</b><span>Podiatric Experts</span></div>
  <div class="stat"><b>3495</b><span>Happy Patients</span></div>
  <div class="stat"><b>100%</b><span>Proven Track Record</span></div>
</section>

<section class="section doctors">
  <div class="wrap" style="height:460px">
    <div class="kicker" style="position:absolute;top:6px">Professional</div>
    <h2 class="subtitle">Our Doctors</h2>
    <div class="arrows"><span>‹</span><span>›</span></div>
    <div class="doc-grid">
      <div class="doc"><div class="ph" role="img" aria-label="Portrait of Lena Groves"></div><div class="inner"><h4>Lena Groves</h4><div class="role">Podiatric Surgeon</div><p>She treats surgically include bunions, hammer toes, neuromas and much other painful foot problems.</p>
        <div class="meta"><div>◉ Harlow Step Podiatry</div><div>✆ (08) 9470 2815</div></div></div></div>
      <div class="doc"><div class="ph" role="img" aria-label="Portrait of Adrian Shore"></div><div class="inner"><h4>Adrian Shore</h4><div class="role">Podiatrist</div><p>He practices in all areas of podiatry, and was a tutor for the Podiatry School at Westmere University.</p>
        <div class="meta"><div>◉ Harlow Step Podiatry</div><div>✆ (08) 9470 2815</div></div></div></div>
      <div class="doc"><div class="ph" role="img" aria-label="Portrait of Tamsin Marlow"></div><div class="inner"><h4>Tamsin Marlow</h4><div class="role">Podiatrist</div><p>Tamsin first attended the clinic as a patient in 2003, which sparked her interest in health care.</p>
        <div class="meta"><div>◉ Harlow Step Podiatry</div><div>✆ (08) 9470 2815</div></div></div></div>
      <div class="doc"><div class="ph" role="img" aria-label="Portrait of Maya Fenwick"></div><div class="inner"><h4>Maya Fenwick</h4><div class="role">Podiatrist</div><p>Maya showed an interest in podiatry from her keen interest in long distance running and dance.</p>
        <div class="meta"><div>◉ Harlow Step Podiatry</div><div>✆ (08) 9470 2815</div></div></div></div>
    </div>
  </div>
</section>

<section class="section cases">
  <div class="wrap" style="height:320px">
    <div class="kicker">Case Histories</div>
    <h2 class="subtitle">Be the first to read</h2>
    <div class="arrows"><span>‹</span><span>›</span></div>
    <div class="case-grid">
      <div class="case"><div class="ph" role="img" aria-label="Foot massage for plantar fascia" style="background:linear-gradient(160deg,#e6d3c5,#b79a86)"></div><h4>Plantar Fascia Case</h4><p>A 40-year-old female presented with pain in her left heel. It had been sore for a long time, but in the last 6 months it had really flared up.</p></div>
      <div class="case"><div class="ph" role="img" aria-label="Podiatrist examining a bunion" style="background:linear-gradient(160deg,#d5e6ef,#e9d3c4)"></div><h4>Bunion Case</h4><p>A 70-year-old female presented to us with severe bunions and overlapping of her 2nd toes. She reported that her feet had bothered her for years.</p></div>
      <div class="case"><div class="ph" role="img" aria-label="Injured foot trauma treatment" style="background:linear-gradient(160deg,#eceae4,#c9bfae)"></div><h4>Trauma Case</h4><p>A 56-year-old gentleman was previously involved in a motorcycle accident in 2003, which caused major trauma to his right foot and leg.</p></div>
    </div>
    <div class="ebook">
      <div class="top"><h4>Podiatric Surgery</h4><p>Dr Lena Groves, Podiatric Surgeon<br>42 Wenlock Road, Kellerton<br>(08) 9470 2815</p></div>
      <div class="ph" role="img" aria-label="Surgeons in an operating theatre" style="background:linear-gradient(160deg,#5c8fa3,#2c5568)"></div>
      <div class="cta">View Our Free Ebook</div>
    </div>
  </div>
</section>

<section class="section booking">
  <div class="wrap" style="height:315px">
    <div class="book">
      <h3>Book an Appointment</h3>
      <div class="fields">
        <div class="field">Departments <span>▾</span></div>
        <div class="field">Doctors <span>▾</span></div>
        <div class="field">Name</div>
        <div class="field">Phone</div>
        <div class="field">Email</div>
        <div class="field">Date <span>▦</span></div>
      </div>
      <span class="btn-outline">Make an Appointment</span>
    </div>
    <div class="faq">
      <div class="kicker">FAQ</div>
      <h2 class="subtitle">Have some Questions?</h2>
      <div class="acc open"><div class="q">Do you have ClaimPoint?<span>−</span></div><div class="a">Yes, we do have ClaimPoint, so you can claim on the spot if you bring your private health card with you.</div></div>
      <div class="acc"><div class="q">Do you offer pensioner discount?<span>+</span></div></div>
      <div class="acc"><div class="q">What does a podiatrist do?<span>+</span></div></div>
      <div class="acc"><div class="q">What is an orthotic and what it is used for?<span>+</span></div></div>
    </div>
  </div>
</section>

<section class="section partners">
  <h3>Partners</h3>
  <div class="logos">
    <span style="width:120px"></span><span style="width:100px"></span><span style="width:140px"></span><span style="width:110px"></span><span style="width:100px"></span>
  </div>
</section>

<section class="section newsletter">
  <h3>Newsletter</h3>
  <p>Subscribe to our newsletter for latest updates</p>
  <div class="nl-form"><div class="in">Email...</div><div class="go">Subscribe</div></div>
</section>

<footer class="section footer">
  <div class="fcols">
    <div class="fcol">
      <h5>Contact Us</h5>
      <div class="cinfo">
        <div>◉ 42 Wenlock Road<br>Kellerton, WA 6099</div>
        <div>✉ info@harlowsteppodiatry.com.au</div>
        <div>⌂ www.harlowsteppodiatry.com.au</div>
        <div>✆ (08) 9470 2815</div>
      </div>
      <div class="fsocial"><i></i><i></i><i></i><i></i></div>
    </div>
    <div class="fcol">
      <h5>Doctors</h5>
      <ul><li>› Lena Groves</li><li>› Adrian Shore</li><li>› Tamsin Marlow</li><li>› Maya Fenwick</li><li>› Kara Whitlow</li><li>› Lauren Kestrel</li></ul>
    </div>
    <div class="fcol">
      <h5>Links</h5>
      <ul><li>› About Us</li><li>› Free Offers</li><li>› Educational Videos</li><li>› Sitemap</li><li>› Privacy Policy</li><li>› Blog</li></ul>
    </div>
    <div class="fcol">
      <h5>Quick Contact</h5>
      <div class="qin">Email</div>
      <div class="qin tall">Message</div>
      <span class="qbtn">Submit</span>
    </div>
  </div>
  <div class="copyright">©Copyright information here</div>
</footer>
<div class="to-top"><svg width="10" height="8" viewBox="0 0 10 8"><path d="M1 7l4-5 4 5" stroke="#fff" stroke-width="1.6" fill="none"/></svg></div>

</body>
</html>
```